Flyer for the Radiant Harvest Worship Day

I am looking to create a flyer for a one day prayer retreat our church is organizing.
This flyer will be posted on social media, websites and will also be printed so it can be mailed to people.
I am looking for something professional, with good use of our logo and band colors (logo colors).
I am counting on the designer's skill, creativity, art and knowledge of media communication to produce a flyer that will effectively and quickly convey the message we are trying to spread.
CONTENT OF THE FLYER:
Event title: Radiant Harvest Worship Day
Date: Tuesday July 2nd, 2019
Time: 11:00AM - 7:00PM
Belmont Hotel, 4875 Maple Ridge Road, Portland, Maine 04219 (Room: Evergreen)
Event Key words to highlight what the event is about: Prayer, Sharing the Word, Panel discussion, prophecy, Impartation.
Key phrases:
A one day prayer retreat.
Jesus Chris is Lord
Contact info:
www.tuvela.org
Phone: 207 583 2194
Email: contact@brookmeadow.org

```html
<!DOCTYPE html>
<html lang="en">
<head>
<meta charset="utf-8">
<title>Radiant Harvest Worship Day</title>
<link href="https://fonts.googleapis.com/css2?family=Cinzel:wght@500&family=Oswald:wght@300;400;600&family=Fira+Sans:wght@400&display=swap" rel="stylesheet">
<style>
  :root {
    --page-bg: #e4e4e4;
    --navy-deep: #0f2b4c;
    --navy: #163a64;
    --blue-panel: #1f4e82;
    --blue-band: #215a91;
    --white: #ffffff;
    --gold-light: #ffd56a;
    --gold: #f7a21e;
    --soft-white: #e8eef6;
  }
  html, body {
    margin: 0;
    width: 1001px;
    height: 1200px;
    overflow: hidden;
    background: var(--page-bg);
  }
  .flyer {
    position: absolute;
    left: 78px;
    top: 0;
    width: 846px;
    height: 1200px;
    background: var(--navy-deep);
    overflow: hidden;
  }
  .panel {
    position: absolute;
    background: linear-gradient(160deg, #2a5f98 0%, var(--blue-panel) 60%, #1a4474 100%);
  }
  .panel--tl { left: 0; top: 0; width: 276px; height: 330px; }
  .panel--tr { left: 570px; top: 0; width: 276px; height: 330px; }
  .panel--bl { left: 0; top: 622px; width: 276px; height: 578px; background: linear-gradient(180deg, #1f4f83, #163c68); }
  .panel--br { left: 570px; top: 622px; width: 276px; height: 578px; background: linear-gradient(180deg, #1f4f83, #173d69); }
  .cross-glow {
    position: absolute;
    left: 150px; top: 250px;
    width: 560px; height: 300px;
    background: radial-gradient(ellipse at center, rgba(110,150,200,0.35), rgba(15,43,76,0) 70%);
  }
  .photo {
    position: absolute;
  }
  .photo--portrait {
    left: 570px; top: 0; width: 276px; height: 330px;
    background: radial-gradient(ellipse at 70% 40%, rgba(120,140,180,0.35), rgba(31,78,130,0) 70%);
  }
  .photo--hands-book {
    left: 0; top: 700px; width: 560px; height: 400px;
    background: radial-gradient(ellipse at 45% 55%, rgba(140,175,220,0.35), rgba(20,50,90,0) 70%);
  }
  .brand {
    position: absolute;
    top: 130px;
    left: 0; right: 0;
    display: flex;
    justify-content: center;
    align-items: center;
    gap: 18px;
  }
  .brand__mark {
    width: 26px; height: 26px;
    border-radius: 50%;
    background: var(--gold);
  }
  .brand__name {
    font-family: "Cinzel", serif;
    font-weight: 500;
    font-size: 108px;
    line-height: 1;
    color: var(--white);
    letter-spacing: 0.01em;
  }
  .title {
    position: absolute;
    left: 0; right: 0;
    text-align: center;
    margin: 0;
    font-family: "Oswald", sans-serif;
  }
  .title__lead {
    position: absolute;
    left: 0; right: 0; top: 345px;
    font-weight: 300;
    font-size: 104px;
    line-height: 1;
    color: var(--white);
    letter-spacing: -0.01em;
    display: block;
  }
  .title__main {
    position: absolute;
    left: 0; right: 0; top: 455px;
    font-weight: 600;
    font-size: 132px;
    line-height: 1;
    letter-spacing: 0.01em;
    display: block;
    background: linear-gradient(180deg, var(--gold-light) 0%, var(--gold) 100%);
    -webkit-background-clip: text;
    background-clip: text;
    color: transparent;
  }
  .tagline {
    position: absolute;
    left: 0; right: 0; top: 648px;
    text-align: center;
    font-family: "Fira Sans", sans-serif;
    font-size: 27px;
    line-height: 40px;
    letter-spacing: 0.2em;
    color: var(--white);
  }
  .tagline p { margin: 0; }
  .event-date {
    position: absolute;
    left: 0; right: 0; top: 925px;
    text-align: center;
    font-family: "Oswald", sans-serif;
    font-weight: 600;
    font-size: 46px;
    line-height: 1.1;
    color: var(--white);
    letter-spacing: -0.01em;
    text-shadow: 0 2px 4px rgba(0,0,0,0.6);
  }
  .event-time {
    position: absolute;
    left: 0; right: 0; top: 1006px;
    text-align: center;
    font-family: "Oswald", sans-serif;
    font-weight: 400;
    font-size: 36px;
    line-height: 1.1;
    color: var(--white);
  }
  .divider {
    position: absolute;
    left: 402px; top: 1068px;
    width: 44px; height: 3px;
    background: var(--white);
  }
  .venue-band {
    position: absolute;
    left: 0; right: 0; top: 1100px;
    height: 58px;
    background: var(--blue-band);
    display: flex;
    align-items: center;
    justify-content: center;
    text-align: center;
    font-family: "Fira Sans", sans-serif;
    font-size: 19px;
    line-height: 27px;
    letter-spacing: 0.02em;
    color: var(--soft-white);
  }
  .venue-band p { margin: 0; }
</style>
</head>
<body>
  <main class="flyer">
    <div class="panel panel--tl"></div>
    <div class="panel panel--tr"></div>
    <div class="panel panel--bl"></div>
    <div class="panel panel--br"></div>
    <div class="cross-glow"></div>
    <div class="photo photo--portrait" role="img" aria-label="Faint devotional portrait photograph blended into the top right corner"></div>
    <div class="photo photo--hands-book" role="img" aria-label="Photograph of folded hands resting on a Bible in blue light"></div>

    <header class="brand">
      <span class="brand__mark"></span>
      <span class="brand__name">TUVELA</span>
    </header>

    <h1 class="title">
      <span class="title__lead">RADIANT HARVEST</span>
      <span class="title__main">WORSHIP DAY</span>
    </h1>

    <div class="tagline">
      <p>A ONE DAY PRAYER RETREAT</p>
      <p>JESUS CHRIS IS LORD</p>
    </div>

    <div class="event-date">TUESDAY JULY 2ND, 2019</div>
    <div class="event-time">11:00AM - 7:00PM</div>
    <div class="divider"></div>

    <footer class="venue-band">
      <div>
        <p>Belmont Hotel, 4875 Maple Ridge Road, Portland,</p>
        <p>Maine 04219 (Room: Evergreen)</p>
      </div>
    </footer>
  </main>
</body>
</html>
```